Tufted Hollow is company name.Handknit&crochet blankets&scarves. Need logo&business ...

I need a design that is eye catching, using yarn and is flowing. I'd like to see colors in aqua (Larkin Peabody paint LP9043 Aquastone) for the yarn and company name. For the text, a dark grey color (Larkin Peabody LP7622 Hamburg Gray)

Colors
87cfc7

```html
<!DOCTYPE html>
<html lang="en">
<head>
<meta charset="utf-8">
<title>Tufted Hollow — Business Cards</title>
<link rel="stylesheet" href="https://fonts.googleapis.com/css2?family=Poppins:wght@300;400&family=Allura&display=swap">
<style>
  :root {
    --aquastone: #87cfc7;
    --hamburg-gray: #5a5a5c;
    --card: #ffffff;
    --backdrop: #e9eaeb;
    --faint: #eeeeee;
  }
  * { margin: 0; padding: 0; box-sizing: border-box; }
  html, body { width: 1200px; height: 880px; overflow: hidden; }
  body {
    background: var(--backdrop);
    font-family: "Poppins", sans-serif;
    color: var(--hamburg-gray);
    display: flex;
    flex-direction: column;
    align-items: center;
    justify-content: center;
    gap: 56px;
  }
  .card {
    position: relative;
    width: 560px;
    height: 320px;
    background: var(--card);
    border-radius: 18px;
    overflow: hidden;
    box-shadow: 0 6px 18px rgba(0,0,0,0.12);
  }
  .brand {
    position: absolute;
    display: flex;
    align-items: center;
    gap: 12px;
    font-family: "Poppins", sans-serif;
    font-weight: 300;
    color: var(--aquastone);
    white-space: nowrap;
  }
  .brand-dot {
    width: 22px; height: 22px;
    border-radius: 50%;
    background: var(--aquastone);
  }
  .card-front .brand {
    left: 50%; top: 50%;
    transform: translate(-50%, -50%);
    font-size: 46px;
  }
  .card-back .brand {
    left: 36px; top: 70px;
    font-size: 38px;
  }
  .faint-circle {
    position: absolute;
    right: -40px; top: -70px;
    width: 300px; height: 300px;
    border-radius: 50%;
    border: 2px solid var(--faint);
  }
  .services {
    position: absolute;
    right: 30px; top: 150px;
    list-style: none;
    text-align: right;
    font-size: 13px;
    line-height: 1.55;
    letter-spacing: 0.3px;
  }
  .services li::after {
    content: "";
    display: inline-block;
    width: 5px; height: 5px;
    margin-left: 8px;
    border-radius: 50%;
    background: var(--aquastone);
    vertical-align: middle;
  }
  .person {
    position: absolute;
    left: 44px; top: 196px;
    font-family: "Allura", cursive;
    font-size: 38px;
    color: var(--hamburg-gray);
  }
  .contact {
    position: absolute;
    left: 44px; top: 246px;
    list-style: none;
    font-size: 14px;
    line-height: 1.6;
  }
  .contact li { display: flex; align-items: center; gap: 10px; }
  .contact svg { width: 16px; height: 16px; flex: none; }
  .edge-band {
    position: absolute;
    left: 0; right: 0; bottom: 0;
    height: 8px;
    background: var(--aquastone);
  }
</style>
</head>
<body>

  <section class="card card-front">
    <div class="brand"><span class="brand-dot"></span>Tufted Hollow</div>
  </section>

  <section class="card card-back">
    <div class="faint-circle"></div>
    <div class="brand"><span class="brand-dot"></span>Tufted Hollow</div>

    <ul class="services">
      <li>Handknit&amp;crochet</li>
      <li>Baby Afghans</li>
      <li>Afghans</li>
      <li>scarves, Gloves,Hats</li>
    </ul>

    <p class="person">Dana Whitcombe</p>

    <ul class="contact">
      <li>
        <svg viewBox="0 0 16 16" aria-hidden="true">
          <circle cx="8" cy="8" r="8" fill="#87cfc7"/>
          <path d="M5.3 4.2l1.3 1.6-.7 1a5 5 0 0 0 2.3 2.3l1-.7 1.6 1.3-.8 1.2c-2.9-.3-5-2.4-5.3-5.3z" fill="#fff"/>
        </svg>
        (555) 214 0387
      </li>
      <li>
        <svg viewBox="0 0 16 16" aria-hidden="true">
          <circle cx="8" cy="8" r="8" fill="#87cfc7"/>
          <rect x="4" y="5.2" width="8" height="5.6" rx="0.6" fill="none" stroke="#fff" stroke-width="1"/>
          <path d="M4.3 5.6L8 8.4l3.7-2.8" fill="none" stroke="#fff" stroke-width="1"/>
        </svg>
        hello@tuftedhollow.com
      </li>
    </ul>

    <div class="edge-band"></div>
  </section>

</body>
</html>
```